Unisex deodorant packaging

we need 12 designs of Unisex deodorant spray, all designs shoud be different.

Brand Name is Verdel. Artwork file size is attached for reference. Logo we can be redesigned.

variants names will be:

Tapestry
Ripple
Lanterns
Meadow
Quarry
Pebble
Tide
Fern
Orchard
Mossy
Vast
Brisk

Target Market(s)

B+, B, C+

Requirements
Must have
• colors, new fonts
Nice to have
• creative work, all 12 designs different

```html
<!DOCTYPE html>
<html lang="en">
<head>
<meta charset="utf-8">
<title>Verdel Brisk – Deodorant Body Spray Label</title>
<link rel="stylesheet" href="https://fonts.googleapis.com/css2?family=Archivo+Narrow:wght@700&family=Lobster&family=Parisienne&family=Varela+Round&display=swap">
<style>
  :root {
    --bg: #2a331a;
    --label-light: #c6df5a;
    --label-mid: #66b43f;
    --label-dark: #2f8a3a;
    --ring: #5bb03f;
    --disc: #ffffff;
    --disc-shade: #dcdcdc;
    --brand-ink: #ffffff;
    --variant-ink: #2e8b2e;
    --script-ink: #2b2530;
    --small-ink: #1e1e1e;
    --leaf-light: #7cc24f;
    --leaf-dark: #2f7d32;
  }
  * { margin: 0; padding: 0; box-sizing: border-box; }
  html, body {
    width: 1200px; height: 1124px; overflow: hidden;
    background: var(--bg);
  }
  .canvas { position: relative; width: 1200px; height: 1124px; }

  .label {
    position: absolute; left: 388px; top: 32px;
    width: 424px; height: 1060px;
    border-radius: 10px;
    overflow: hidden;
    background:
      radial-gradient(ellipse 70% 45% at 50% 38%, var(--label-light) 0%, rgba(198,223,90,0) 70%),
      linear-gradient(90deg, var(--label-dark) 0%, var(--label-mid) 22%, var(--label-mid) 70%, var(--label-dark) 100%);
  }

  .brand {
    position: absolute; top: 168px; left: 0; width: 100%;
    text-align: center;
    font-family: "Varela Round", sans-serif;
    font-size: 62px; line-height: 1;
    color: var(--brand-ink);
  }

  .badge { position: absolute; left: 0; top: 0; width: 424px; height: 760px; }

  .variant {
    position: absolute; top: 395px; left: 0; width: 100%;
    text-align: center;
    font-family: "Lobster", cursive;
    font-size: 118px; line-height: 1;
    color: var(--variant-ink);
  }

  .sprig {
    position: absolute; left: 62px; top: 540px;
    width: 300px; height: 180px;
    border-radius: 50% 50% 45% 45% / 40% 40% 60% 60%;
    background: radial-gradient(ellipse at 50% 40%, var(--leaf-light), var(--leaf-dark));
  }

  .descriptor {
    position: absolute; top: 762px; left: 0; width: 100%;
    text-align: center;
    font-family: "Parisienne", cursive;
    font-size: 58px; line-height: 68px;
    color: var(--script-ink);
  }

  .volume {
    position: absolute; top: 938px; left: 0; width: 100%;
    text-align: center;
    font-family: "Archivo Narrow", sans-serif;
    font-weight: 700; font-size: 32px;
    color: var(--small-ink);
  }
</style>
</head>
<body>
<main class="canvas">
  <section class="label">
    <div class="brand">Verdel</div>

    <svg class="badge" viewBox="0 0 424 760" aria-hidden="true">
      <defs>
        <radialGradient id="discShade" cx="45%" cy="40%" r="65%">
          <stop offset="0%" stop-color="var(--disc)"/>
          <stop offset="75%" stop-color="var(--disc)"/>
          <stop offset="100%" stop-color="var(--disc-shade)"/>
        </radialGradient>
      </defs>
      <circle cx="213" cy="469" r="190" fill="var(--ring)"/>
      <circle cx="213" cy="469" r="176" fill="url(#discShade)"/>
      <circle cx="36" cy="378" r="32" fill="url(#discShade)"/>
      <circle cx="380" cy="455" r="12" fill="url(#discShade)"/>
    </svg>

    <div class="variant">Brisk</div>

    <div class="sprig" role="img" aria-label="Fresh green leaves with dew drops"></div>

    <div class="descriptor">Deodorant<br>Body Spray</div>

    <div class="volume">150ml Net 5.1 fl. oz.</div>
  </section>
</main>
</body>
</html>
```